Brisk Telecom Branding and Visual Identity Project

We need some visual identity items for Brisk Telecom, which should be produced based on the company's logo attached.

I would like the brochure to be as lightweight as possible so that it can be sent via email.

Below are the items we need to be made.

- Company letterhead
- Company brochure in PDF format (single page)
- Email signature (only one)
- Wallpaper
- Banner for use on social media
- Customized shirt

Target Market(s)

Passengers and crew members of ships

Industry/Entity Type

Telecom & Maritime

Colors
0054AA
0677BA
7BADD7
CADEEF
E8F1F8

Requirements
Nice to have
• Colors that match the logo
Should not have
• Colors that clash with the logo colors

```html
<!DOCTYPE html>
<html lang="en">
<head>
<meta charset="utf-8">
<title>Brisk Telecom – Email Signature</title>
<link rel="stylesheet" href="https://fonts.googleapis.com/css2?family=Questrial&family=Raleway:wght@700&family=Roboto:wght@400&display=swap">
<style>
  :root {
    --backdrop: #e6e7e9;
    --card: #ffffff;
    --brand-blue: #0677ba;
    --brand-deep: #0054aa;
    --brand-sky: #7badd7;
    --text-grey: #555555;
    --rule-grey: #c8c8c8;
    --title-ink: #111111;
  }
  * { box-sizing: border-box; margin: 0; padding: 0; }
  html, body {
    width: 1200px;
    height: 1000px;
    overflow: hidden;
    background: var(--backdrop);
  }
  .stage {
    position: relative;
    width: 1200px;
    height: 1000px;
  }
  .stage-title {
    position: absolute;
    top: 178px;
    left: 0;
    width: 1200px;
    text-align: center;
    font-family: "Questrial", sans-serif;
    font-size: 46px;
    letter-spacing: 1px;
    color: var(--title-ink);
  }
  .signature-card {
    position: absolute;
    left: 217px;
    top: 366px;
    width: 766px;
    height: 268px;
    background: var(--card);
    box-shadow: 5px 6px 8px rgba(0, 0, 0, 0.28);
  }
  .brand-mark {
    position: absolute;
    left: 73px;
    top: 110px;
    width: 200px;
    font-family: "Roboto", sans-serif;
    font-weight: 400;
    font-size: 31px;
    color: var(--brand-blue);
    text-align: center;
    line-height: 1.1;
  }
  .divider {
    position: absolute;
    left: 297px;
    top: 55px;
    width: 2px;
    height: 158px;
    background: var(--rule-grey);
  }
  .details {
    position: absolute;
    left: 326px;
    top: 54px;
    font-family: "Roboto", sans-serif;
    color: var(--text-grey);
    font-size: 18.5px;
    line-height: 23px;
  }
  .person-name {
    font-family: "Raleway", sans-serif;
    font-weight: 700;
    font-size: 20px;
    color: var(--brand-blue);
    line-height: 24px;
  }
  .person-role { margin-bottom: 10px; }
  .company-name { color: var(--brand-blue); margin-left: -2px; }
  .address { margin-left: -2px; margin-bottom: 9px; }
  .sep { color: var(--brand-blue); }
  .social-row {
    position: absolute;
    right: 34px;
    top: 216px;
    display: flex;
    gap: 7px;
  }
  .social-dot {
    width: 22px;
    height: 22px;
    border-radius: 50%;
  }
  .social-dot.one { background: var(--brand-deep); }
  .social-dot.two { background: var(--brand-sky); }
  .social-dot.three { background: var(--brand-blue); }
  .social-dot.four { background: var(--brand-deep); }
</style>
</head>
<body>
<main class="stage">
  <h1 class="stage-title">HTML EMAIL SIGNATURE</h1>

  <section class="signature-card">
    <div class="brand-mark">Brisk Telecom</div>
    <div class="divider"></div>

    <div class="details">
      <p class="person-name">DANA WHITLOCK</p>
      <p class="person-role">Founder</p>
      <p class="company-name">Brisk Telecom, LLC</p>
      <p class="address">48 Harbor Road, Suite 5 Salem, MA 01970</p>
      <p class="contact">T : (555) 013-4829 <span class="sep">|</span> E : hello@brisktel.com</p>
      <p class="website">www.brisktel.com</p>
    </div>

    <div class="social-row" aria-label="Social links">
      <span class="social-dot one"></span>
      <span class="social-dot two"></span>
      <span class="social-dot three"></span>
      <span class="social-dot four"></span>
    </div>
  </section>
</main>
</body>
</html>
```